Modern Lawfirm Business Card Design

We're looking for a business card to incorporate the newly created logo we had made.

Ideally looking for a law firm business card demonstrating, modern, minimalist, strong/bold design.

I'm open to any design honestly, but nothing "flashy".

Target Market(s)

Immigration law, family immigration, humanitarian, general legal

Industry/Entity Type

Law Firm

Contact Information for Business Card

Please use dummy information, name, street address, city, state, phone number, email, website.

Font styles to use
Serif
Sans Serif

Requirements
Must have
• Please use dummy information, name, street address, city, state, phone number, email, website.

```html
<!DOCTYPE html>
<html lang="en">
<head>
<meta charset="utf-8">
<title>Calloway Immigration Law – Business Card</title>
<link href="https://fonts.googleapis.com/css2?family=Lato:wght@400;700&display=swap" rel="stylesheet">
<style>
  :root {
    --brand-blue: #3f5e9c;
    --card-white: #ffffff;
    --ink: #1c1c1c;
    --stage: #d9dadc;
  }
  * { margin: 0; padding: 0; box-sizing: border-box; }
  html, body { width: 1200px; height: 900px; overflow: hidden; }
  body {
    background: var(--stage);
    font-family: 'Lato', sans-serif;
    position: relative;
  }
  .card {
    position: absolute;
    width: 700px;
    height: 400px;
    box-shadow: 0 6px 18px rgba(0,0,0,0.18);
    overflow: hidden;
  }
  /* Back side */
  .card-back {
    left: 440px; top: 50px;
    background: var(--brand-blue);
    color: var(--card-white);
    display: flex; flex-direction: column;
    align-items: center; justify-content: center;
  }
  .brand-name {
    font-weight: 700;
    font-size: 40px;
    letter-spacing: 1px;
    text-transform: uppercase;
    text-align: center;
    line-height: 1.15;
  }
  .card-back .brand-name { color: var(--card-white); }
  .card-back .site {
    margin-top: 48px;
    font-size: 18px;
    letter-spacing: 4px;
  }
  /* Front side */
  .card-front {
    left: 60px; top: 460px;
    background: var(--card-white);
  }
  .card-front .brand-name {
    position: absolute;
    left: 44px; top: 48px;
    color: var(--brand-blue);
    font-size: 30px;
    text-align: left;
  }
  .accent-bar {
    position: absolute;
    right: 0; top: 170px;
    width: 20px; height: 230px;
    background: var(--brand-blue);
  }
  .contact {
    position: absolute;
    right: 52px; top: 150px;
    text-align: right;
    color: var(--ink);
  }
  .contact .person-name {
    color: var(--brand-blue);
    font-weight: 700;
    font-size: 26px;
  }
  .contact .role { font-size: 18px; margin-bottom: 14px; }
  .contact .address { font-size: 18px; line-height: 1.3; margin-bottom: 14px; }
  .contact-line {
    display: flex; justify-content: flex-end; align-items: center;
    gap: 10px; font-size: 18px; line-height: 1.35;
  }
  .contact-line svg { width: 16px; height: 16px; fill: var(--brand-blue); }
</style>
</head>
<body>
  <section class="card card-back">
    <div class="brand-name">Calloway Immigration Law</div>
    <div class="site">www.calloway-law.com</div>
  </section>

  <section class="card card-front">
    <div class="brand-name">Calloway Immigration Law</div>
    <div class="accent-bar"></div>
    <div class="contact">
      <div class="person-name">Daniel Reyes</div>
      <div class="role">Manager</div>
      <div class="address">4100 Elm Row<br>Lakeside TX 78000</div>
      <div class="contact-line">512 004 2300
        <svg viewBox="0 0 16 16" aria-hidden="true"><path d="M3 1l3 3-2 2c1 2 3 4 5 5l2-2 3 3-2 2C7 14 2 9 1 3z"/></svg>
      </div>
      <div class="contact-line">512 004 2301
        <svg viewBox="0 0 16 16" aria-hidden="true"><rect x="4" y="1" width="8" height="4"/><rect x="1" y="6" width="14" height="6" rx="1"/><rect x="4" y="10" width="8" height="5" fill="#fff" stroke="#3f5e9c" stroke-width="1.5"/></svg>
      </div>
      <div class="contact-line">info@calloway-law.com
        <svg viewBox="0 0 16 16" aria-hidden="true"><rect x="1" y="3" width="14" height="10"/><path d="M1 3l7 6 7-6" fill="none" stroke="#fff" stroke-width="1.5"/></svg>
      </div>
      <div class="contact-line">www.calloway-law.com
        <svg viewBox="0 0 16 16" aria-hidden="true"><circle cx="8" cy="8" r="7"/><path d="M1 8h14M8 1v14M3 4h10M3 12h10" stroke="#fff" stroke-width="1" fill="none"/><ellipse cx="8" cy="8" rx="3" ry="7" fill="none" stroke="#fff" stroke-width="1"/></svg>
      </div>
    </div>
  </section>
</body>
</html>
```